Contractor Business Card Design

Looking to have a card made that has a bold description of (KITCHENS, BASEMENTS, BATHROOMS)

Definition and layers a plus

Contact info is;

Mark T. Ellery
Lakeview, MN 55012
Cell: 612-555-0147
website: www.cobaltfinishworks.example
Email: cobaltfinishworksmn@mailbox.example

colors: red, black, gray, white

Contact Information for Business Card

Contact info is;

Mark T. Ellery
Lakeview, MN 55012
Cell: 612-555-0147

Colors
ec1f27

Requirements
Must have
• Looking for layers and definition
Nice to have
• Cards are planned to be printed on plastic cards

```html
<!DOCTYPE html>
<html lang="en">
<head>
<meta charset="utf-8">
<title>Cobalt Finish Works – Business Card</title>
<link href="https://fonts.googleapis.com/css2?family=Montserrat:wght@400;500;700&display=swap" rel="stylesheet">
<style>
  :root {
    --backdrop: #4b5053;
    --card-gray: #d1d1d2;
    --ink: #0b0b0c;
    --white: #ffffff;
    --red: #ec1f27;
  }
  * { box-sizing: border-box; margin: 0; padding: 0; }
  html, body { width: 1200px; height: 1050px; overflow: hidden; }
  body {
    background: var(--backdrop);
    font-family: "Montserrat", Arial, sans-serif;
    position: relative;
  }
  .card {
    position: absolute;
    left: 190px;
    width: 820px;
    height: 460px;
    overflow: hidden;
    box-shadow: 0 10px 24px rgba(0,0,0,0.35);
  }
  .card--front { top: 40px; background: var(--card-gray); }
  .card--back { top: 550px; background: var(--ink); }

  .service-band {
    position: absolute;
    left: 0; right: 0; bottom: 0;
    height: 114px;
    display: flex;
    align-items: center;
    justify-content: center;
    gap: 24px;
    font-size: 31px;
    font-weight: 400;
    letter-spacing: 2.5px;
    text-transform: uppercase;
  }
  .card--front .service-band { background: var(--ink); color: var(--white); }
  .card--back .service-band { background: var(--card-gray); color: var(--ink); }
  .service-band .dot { font-weight: 700; }

  .brand {
    position: absolute;
    display: flex;
    flex-direction: column;
    align-items: center;
  }
  .brand__circle { display: block; }
  .brand__name {
    margin-top: 14px;
    font-weight: 700;
    font-size: 30px;
    line-height: 1.15;
    letter-spacing: 3px;
    text-align: center;
    text-transform: uppercase;
  }
  .card--front .brand { left: 30px; top: 52px; width: 300px; }
  .card--front .brand__name { color: var(--ink); }
  .card--back .brand { left: 0; right: 0; top: 58px; }
  .card--back .brand__name { color: var(--white); }

  .contact {
    position: absolute;
    left: 368px;
    top: 64px;
    color: var(--ink);
  }
  .contact__name {
    font-size: 31px;
    font-weight: 700;
    margin-bottom: 22px;
    letter-spacing: 0.5px;
  }
  .contact__list { list-style: none; }
  .contact__item {
    display: flex;
    align-items: center;
    gap: 14px;
    font-size: 19px;
    font-weight: 400;
    height: 51px;
    white-space: nowrap;
  }
  .contact__icon { width: 28px; height: 28px; flex: none; }
</style>
</head>
<body>

  <section class="card card--front" aria-label="Business card front">
    <div class="brand">
      <svg class="brand__circle" width="150" height="150" viewBox="0 0 150 150" aria-hidden="true">
        <circle cx="75" cy="75" r="68" fill="none" stroke="#ec1f27" stroke-width="5"/>
      </svg>
      <div class="brand__name">Cobalt<br>Finish Works</div>
    </div>

    <div class="contact">
      <h1 class="contact__name">Mark T. Ellery</h1>
      <ul class="contact__list">
        <li class="contact__item">
          <svg class="contact__icon" viewBox="0 0 24 24" aria-hidden="true"><path fill="#0b0b0c" d="M6.6 2.5c.6-.3 1.2-.1 1.5.4l2 3.4c.3.5.2 1.1-.2 1.5L8.5 9c.9 2.4 3.1 4.8 5.7 6.2l1.3-1.4c.4-.4 1-.5 1.5-.2l3.4 2c.5.3.7 1 .4 1.5l-1.1 2.2c-.4.8-1.300 1.2-2.2 1C10.9 18.9 5.2 12.8 3.9 6.1c-.2-.9.3-1.8 1.1-2.2z"/></svg>
          <span>612-555-0147</span>
        </li>
        <li class="contact__item">
          <svg class="contact__icon" viewBox="0 0 24 24" aria-hidden="true"><rect x="2.5" y="5" width="19" height="14" fill="none" stroke="#0b0b0c" stroke-width="1.8"/><path d="M2.5 5 12 13l9.5-8M2.5 19l7-6.5M21.5 19l-7-6.5" fill="none" stroke="#0b0b0c" stroke-width="1.6"/></svg>
          <span>cobaltfinishworksmn@mailbox.example</span>
        </li>
        <li class="contact__item">
          <svg class="contact__icon" viewBox="0 0 24 24" aria-hidden="true"><g fill="none" stroke="#0b0b0c" stroke-width="1.6"><circle cx="12" cy="12" r="9.5"/><ellipse cx="12" cy="12" rx="4.2" ry="9.5"/><path d="M2.5 12h19M4 7h16M4 17h16"/></g></svg>
          <span>www.cobaltfinishworks.example</span>
        </li>
        <li class="contact__item">
          <svg class="contact__icon" viewBox="0 0 24 24" aria-hidden="true"><path fill="#0b0b0c" d="M12 1.5a6 6 0 0 1 6 6c0 4.2-6 10.5-6 10.5S6 11.7 6 7.5a6 6 0 0 1 6-6zm0 3.5a2.5 2.5 0 1 0 0 5 2.5 2.5 0 0 0 0-5z"/><ellipse cx="12" cy="20" rx="8" ry="2.6" fill="none" stroke="#0b0b0c" stroke-width="1.6"/></svg>
          <span>Lakeview, MN 55012</span>
        </li>
      </ul>
    </div>

    <div class="service-band">
      <span>Kitchens</span><span class="dot">.</span><span>Basements</span><span class="dot">.</span><span>Bathrooms</span>
    </div>
  </section>

  <section class="card card--back" aria-label="Business card back">
    <div class="brand">
      <svg class="brand__circle" width="140" height="140" viewBox="0 0 140 140" aria-hidden="true">
        <circle cx="70" cy="70" r="63" fill="none" stroke="#ec1f27" stroke-width="5"/>
      </svg>
      <div class="brand__name">Cobalt<br>Finish Works</div>
    </div>

    <div class="service-band">
      <span>Kitchens</span><span class="dot">.</span><span>Basements</span><span class="dot">.</span><span>Bathrooms</span>
    </div>
  </section>

</body>
</html>
```